Unique malt liquor beverage needs a logo design and bottle (6.9oz clear glass flask) label designed.

We need a logo and bottle label design for our new beverage here at Brightwell Drinks, a new company based in West Virginia. This is a differentiated product in that we use only natural ingredients and deliver it in a novel 6.9oz glass flask. Our new beverage is a naturally flavored malt liquor drink that we call "Tumbler". Our proposed tag line will be "Made to Tumble" or "Bold Tip. Quick Tumble". We want a logo and bottle label design that differentiates us even further.

Target Market(s)

See images I uploaded to see our two competitors...we need to be better than this but it gives you idea of the spirit of this beverage class.

Industry/Entity Type

Alcohol beverage

Requirements
Must have
• Label needs to include “14% alc/vol 6.9 oz” Both of these elements can be small and at bottom of front face of label. Also must look great on clear glass flask.
Should not have
• Do not put "malt liquor" on label. Under "Tumbler" name it will need to state "Alcoholic Beverage"

```html
<!DOCTYPE html>
<html lang="en">
<head>
<meta charset="utf-8">
<title>Tumbler Label</title>
<link rel="stylesheet" href="https://fonts.googleapis.com/css2?family=Oswald:wght@400;600&family=Josefin+Sans:wght@400&family=Archivo+Black&family=Bitter:wght@500&family=Noto+Serif:wght@700&display=swap">
<style>
  :root {
    --paper: #ffffff;
    --tan: #c9a070;
    --tan-dark: #b48a5c;
    --band-grey: #cdced2;
    --ink: #1c1a1a;
    --red: #9b1424;
    --red-light: #c21f33;
    --orange: #f7941d;
    --white: #ffffff;
    --portrait-a: #8a6a4d;
    --portrait-b: #3b2c22;
  }
  html, body {
    margin: 0;
    width: 1200px;
    height: 1200px;
    overflow: hidden;
    background: var(--paper);
  }
  .label-art {
    display: block;
    width: 1200px;
    height: 1200px;
  }
  .brand-name {
    font-family: "Oswald", sans-serif;
    font-weight: 600;
    fill: var(--ink);
  }
  .category {
    font-family: "Josefin Sans", sans-serif;
    font-weight: 400;
    fill: var(--white);
    letter-spacing: 2px;
  }
  .seal-name {
    font-family: "Noto Serif", serif;
    font-weight: 700;
    fill: var(--orange);
    letter-spacing: 3px;
  }
  .tagline {
    font-family: "Bitter", serif;
    font-weight: 500;
    fill: var(--white);
  }
  .flavour-note {
    font-family: "Archivo Black", sans-serif;
    fill: var(--ink);
    letter-spacing: 5px;
  }
  .fine-print {
    font-family: "Oswald", sans-serif;
    font-weight: 400;
    fill: var(--ink);
  }
  .panel { fill: var(--tan); }
  .band-frame { fill: var(--tan); }
  .band-face { fill: var(--band-grey); }
  .band-strip { fill: var(--red); }
  .seal-rim { fill: var(--tan); }
  .seal-ring { fill: var(--ink); }
  .stamp { fill: var(--ink); }
</style>
</head>
<body>
<svg class="label-art" viewBox="455 630 1000 1000" xmlns="http://www.w3.org/2000/svg">
  <defs>
    <radialGradient id="portrait-tone" cx="50%" cy="40%" r="60%">
      <stop offset="0%" stop-color="var(--portrait-a)"/>
      <stop offset="100%" stop-color="var(--portrait-b)"/>
    </radialGradient>
    <linearGradient id="strip-tone" x1="0" y1="0" x2="1" y2="0">
      <stop offset="0%" stop-color="var(--red)"/>
      <stop offset="60%" stop-color="var(--red-light)"/>
      <stop offset="100%" stop-color="var(--red)"/>
    </linearGradient>
    <path id="seal-arc" d="M 828.1 781.8 A 135 135 0 1 0 1081.9 781.8"/>
  </defs>

  <!-- lower info panel -->
  <path class="panel" d="M795 1260 H1117 V1580 Q1117 1602 1095 1602 H817 Q795 1602 795 1580 Z"/>

  <!-- slanted name band -->
  <polygon class="band-frame" points="678,995 1230,898 1232,1262 680,1350"/>
  <polygon class="band-face" points="689,1003 1221,909 1221,1192 689,1286"/>
  <polygon class="band-strip" style="fill:url(#strip-tone)" points="689,1286 1221,1192 1221,1252 689,1340"/>

  <text class="brand-name" x="955" y="1195" font-size="250" text-anchor="middle"
        textLength="470" lengthAdjust="spacingAndGlyphs"
        transform="rotate(-10 955 1100)">TUMBLER</text>
  <text class="category" x="952" y="1295" font-size="42" text-anchor="middle"
        textLength="460" lengthAdjust="spacingAndGlyphs"
        transform="rotate(-10 952 1280)">ALCOHOLIC BEVERAGE</text>

  <!-- maker seal -->
  <circle class="seal-rim" cx="955" cy="828" r="158"/>
  <circle class="seal-ring" cx="955" cy="828" r="146"/>
  <circle cx="955" cy="818" r="102" fill="url(#portrait-tone)" role="img"
          aria-label="Illustrated portrait of a bearded frontiersman in a wide-brimmed hat"/>
  <text class="seal-name" font-size="24">
    <textPath href="#seal-arc" startOffset="50%" text-anchor="middle">BRIGHTWELL DRINKS</textPath>
  </text>

  <!-- tagline stamp -->
  <rect class="stamp" x="896" y="1302" width="117" height="148"/>
  <text class="tagline" x="954.5" y="1350" font-size="40" text-anchor="middle" textLength="96" lengthAdjust="spacingAndGlyphs">MADE</text>
  <text class="tagline" x="954.5" y="1392" font-size="40" text-anchor="middle">TO</text>
  <text class="tagline" x="954.5" y="1434" font-size="40" text-anchor="middle" textLength="100" lengthAdjust="spacingAndGlyphs">TUMBLE</text>

  <text class="flavour-note" x="950" y="1482" font-size="22" text-anchor="middle">NATURALLY</text>
  <text class="flavour-note" x="950" y="1507" font-size="22" text-anchor="middle">FLAVORED</text>

  <!-- fine print row -->
  <text class="fine-print" x="816" y="1558" font-size="20">14%</text>
  <text class="fine-print" x="816" y="1578" font-size="20">alc/vol</text>
  <text class="fine-print" x="952" y="1552" font-size="32" text-anchor="middle">WEST</text>
  <text class="fine-print" x="952" y="1588" font-size="32" text-anchor="middle">VIRGINIA</text>
  <text class="fine-print" x="1072" y="1552" font-size="22" text-anchor="middle">6.9</text>
  <text class="fine-print" x="1072" y="1578" font-size="22" text-anchor="middle">OZ</text>
</svg>
</body>
</html>
```